Real Estate Development, Finance and Fund Management company

We need a business card and logo design for a new company based in Asia called 'Calloway Vance Ltd.'
We provide full service large scale real estate development services, including fund management, project delivery services and acquisitions. We are looking for a bold logo with a strong feeling of security. A good reference would be the Thornvale (www.thornvalehq.com) or Essenby Capital (www.essenbycap.com).
We will need to have the imagery for the cards and logos to be produced for a dark and light background, and for web and print quality.
Initial thoughts are to have silver text on a black or dark grey background but leave that to your discretion.
Final design should communicate stability, financial safety and building on a solid foundation.
NOTE : We are not looking for pictures or clip art. Logo should be primarily from text and anything additional should be limited and tasteful.
Thanks!

```html
<!DOCTYPE html>
<html lang="en">
<head>
<meta charset="utf-8">
<title>Calloway Vance Ltd. — Business Card</title>
<link href="https://fonts.googleapis.com/css2?family=Arimo:wght@400;700&display=swap" rel="stylesheet">
<style>
  :root {
    --backdrop: #b9babc;
    --card-dark: #4a4b4d;
    --card-light: #f4f4f4;
    --ink-dark: #505153;
    --ink-light: #f4f4f4;
    --accent: #1fa3e0;
    --rule-dark: #5a5b5d;
    --rule-light: #d9d9d9;
  }
  * { box-sizing: border-box; margin: 0; padding: 0; }
  html, body { width: 1200px; height: 900px; overflow: hidden; }
  body {
    background: var(--backdrop);
    font-family: "Arimo", Arial, sans-serif;
    position: relative;
  }
  .card {
    position: absolute;
    width: 620px;
    height: 354px;
    box-shadow: 0 6px 18px rgba(0,0,0,0.25);
  }
  .card--front { left: 80px; top: 70px; background: var(--card-dark); }
  .card--back { left: 80px; top: 476px; background: var(--card-light); }

  .wordmark {
    font-weight: 700;
    text-transform: uppercase;
    line-height: 1.05;
    text-align: center;
    letter-spacing: 1px;
  }
  .wordmark__line { display: block; }
  .wordmark__rule { display: block; height: 2px; margin-top: 8px; }

  .card--front .wordmark {
    position: absolute; left: 170px; top: 105px; width: 280px;
    color: var(--ink-light); font-size: 34px;
  }
  .card--front .wordmark__rule { background: var(--ink-light); }
  .front-url {
    position: absolute; left: 170px; top: 230px; width: 280px;
    text-align: center; color: var(--accent); font-size: 15px; letter-spacing: 0.5px;
  }

  .card--back .wordmark {
    position: absolute; left: 40px; top: 122px; width: 230px;
    color: var(--ink-dark); font-size: 28px;
  }
  .card--back .wordmark__rule { background: var(--ink-dark); }

  .contact {
    position: absolute; left: 305px; top: 62px; width: 290px;
    font-size: 13px; color: #3a3a3a; line-height: 1.3;
  }
  .contact__block { padding-left: 14px; margin-bottom: 12px; position: relative; }
  .contact__block::before {
    content: ""; position: absolute; left: 0; top: 2px; bottom: 2px;
    width: 2px; background: var(--ink-dark);
  }
  .contact__block--accent::before { background: var(--accent); }
  .contact__name { color: var(--accent); font-size: 16px; letter-spacing: 0.5px; text-transform: uppercase; }
  .contact__company { color: var(--accent); }
  .contact__label { color: var(--accent); }
  .contact__email-user { color: var(--accent); }

  .lockup {
    position: absolute; right: 60px; width: 150px;
    font-size: 24px;
  }
  .lockup--dark { top: 40px; color: var(--ink-dark); }
  .lockup--dark .wordmark__rule { background: var(--ink-dark); }
  .lockup--light { top: 140px; color: var(--ink-light); }
  .lockup--light .wordmark__rule { background: var(--ink-light); }
</style>
</head>
<body>
  <section class="card card--front" aria-label="Business card front">
    <div class="wordmark">
      <span class="wordmark__line">Calloway</span>
      <span class="wordmark__line">Vance Ltd.</span>
      <span class="wordmark__rule"></span>
    </div>
    <p class="front-url">www.callowayvance.com</p>
  </section>

  <section class="card card--back" aria-label="Business card back">
    <div class="wordmark">
      <span class="wordmark__line">Calloway</span>
      <span class="wordmark__line">Vance Ltd.</span>
      <span class="wordmark__rule"></span>
    </div>
    <div class="contact">
      <div class="contact__block">
        <p class="contact__name">Mara Ellison</p>
        <p>The Boss</p>
      </div>
      <div class="contact__block contact__block--accent">
        <p class="contact__company">Calloway Vance Ltd.</p>
        <p>88 Harbour Row,</p>
        <p>Suite 40 | Kowloon Bay, HK</p>
      </div>
      <div class="contact__block contact__block--accent">
        <p><span class="contact__label">P :</span> 555.010.2233</p>
        <p><span class="contact__label">F :</span> 555.010.2244</p>
        <p><span class="contact__email-user">mara</span>@callowayvance.com</p>
      </div>
      <div class="contact__block">
        <p>www.callowayvance.com</p>
      </div>
    </div>
  </section>

  <div class="wordmark lockup lockup--dark" aria-label="Wordmark for light backgrounds">
    <span class="wordmark__line">Calloway</span>
    <span class="wordmark__line">Vance Ltd.</span>
    <span class="wordmark__rule"></span>
  </div>
  <div class="wordmark lockup lockup--light" aria-label="Wordmark for dark backgrounds">
    <span class="wordmark__line">Calloway</span>
    <span class="wordmark__line">Vance Ltd.</span>
    <span class="wordmark__rule"></span>
  </div>
</body>
</html>
```